Pat Greene Billboard

**Task Description: Billboard Design for Self Storage Facility**

**Objective:**
Design a captivating billboard to promote our self-storage facility with a focus on our convenient location and online rental capabilities.

**Key Messages to Include:**
1. **Location Emphasis:** Highlight that our facility is located right beside the billboard (maybe by using an arrow pointing left).
2. **Online Rental Convenience:** Feature prominently that customers can "Rent Online Anytime!” or that we are "Always Open Online!"

**Target Audience:**
- Local residents looking for convenient self-storage solutions.
- Businesses needing storage space accessible around the clock.

**Design Elements:**
1. **Visual Impact:** Eye-catching graphics and colors that stand out against the surroundings.
2. **Clear Text:** Bold and concise messaging that can be read and understood quickly.
3. **Contact Information:** Include our phone number and website URL for easy access to further information.

**Additional Information:**
- Billboard dimensions: 12 ft. x 24 ft.
- Preferred color scheme: Bright and attention-grabbing, but professional.
- Branding: Incorporate our logo and brand colors to maintain consistency.

**Deliverables:**
- High-resolution digital file compatible with billboard printing specifications.
- Consider mockups or visualizations for presentation purposes.

Please note that I have attached current logos/graphics that we would love to incorporate into the billboard as well as a picture of our current billboard. Our logo (Pat Greene Self Storage - PG navy.png) MUST be incorporated into the billboard. Also feel free to add any of the current descriptions from the picture of our current billboard into the design. Instead of using "Climate Controlled" use "Temperature Controlled". Thank you for your attention to these details. We look forward to reviewing your proposed design!

```html
<!DOCTYPE html>
<html lang="en">
<head>
<meta charset="utf-8">
<title>Pat Greene Billboard</title>
<link href="https://fonts.googleapis.com/css2?family=Barlow+Semi+Condensed:wght@700&family=Open+Sans:wght@400;600&display=swap" rel="stylesheet">
<style>
  :root {
    --navy: #1c2a5c;
    --paper: #f4f4f2;
    --tan: #a98a5e;
    --backdrop: #dfe3e8;
    --screen-dark: #3b4250;
    --screen-light: #8d96a6;
  }
  * { margin: 0; padding: 0; box-sizing: border-box; }
  html, body { width: 1200px; height: 800px; overflow: hidden; background: var(--backdrop); }
  .billboard {
    position: absolute; left: 20px; top: 110px; width: 1160px; height: 580px;
    background: var(--paper); color: var(--navy);
    font-family: "Open Sans", sans-serif;
  }
  .headline {
    position: absolute; left: 40px; top: 28px;
    font-family: "Barlow Semi Condensed", sans-serif; font-weight: 700;
    font-size: 92px; line-height: 84px; letter-spacing: -1px; text-transform: uppercase;
  }
  .service-band {
    position: absolute; left: 34px; top: 214px; width: 476px; height: 104px;
    background: var(--navy); color: var(--paper);
    font-family: "Barlow Semi Condensed", sans-serif; font-weight: 700;
    font-size: 64px; letter-spacing: 4px; line-height: 104px; text-align: center;
  }
  .features { position: absolute; left: 54px; top: 330px; list-style: none; }
  .features li {
    font-size: 28px; line-height: 40px; text-transform: uppercase;
    display: flex; align-items: center; gap: 12px;
  }
  .features li::before {
    content: ""; width: 16px; height: 16px; background: var(--tan); flex: none;
  }
  .brand-name {
    position: absolute; left: 40px; top: 460px; width: 470px; text-align: center;
    font-family: "Barlow Semi Condensed", sans-serif; font-weight: 700;
    text-transform: uppercase; color: var(--navy);
  }
  .brand-name .name { font-size: 68px; line-height: 68px; display: block; }
  .brand-name .type { font-size: 30px; line-height: 40px; letter-spacing: 14px; display: block; }
  .phone {
    position: absolute; left: 625px; top: 30px;
    display: flex; align-items: center; gap: 22px;
    font-size: 68px; line-height: 80px;
  }
  .devices {
    position: absolute; left: 630px; top: 130px; width: 440px; height: 270px;
    background: linear-gradient(135deg, var(--screen-light), var(--screen-dark));
    border-radius: 10px;
  }
  .location-arrow { position: absolute; left: 530px; top: 400px; }
  .address {
    position: absolute; left: 600px; top: 424px; width: 500px; color: var(--paper);
    display: flex; align-items: center; gap: 12px;
    font-size: 34px; line-height: 50px; text-transform: uppercase; letter-spacing: 1px;
    white-space: nowrap;
  }
  .website {
    position: absolute; left: 660px; top: 512px;
    display: flex; align-items: center; gap: 14px;
    font-size: 36px; line-height: 48px; letter-spacing: 1px;
  }
</style>
</head>
<body>
<main class="billboard">
  <h1 class="headline">Rent Online<br>Anytime!</h1>
  <div class="service-band">SELF STORAGE</div>
  <ul class="features">
    <li>Large/Small Units</li>
    <li>Temperature Controlled</li>
    <li>Covered Boat/ RV Parking</li>
  </ul>
  <div class="brand-name">
    <span class="name">Pat Greene</span>
    <span class="type">Self Storage</span>
  </div>

  <div class="phone">
    <svg width="54" height="54" viewBox="0 0 54 54" aria-hidden="true">
      <rect width="54" height="54" rx="6" fill="var(--navy)"/>
      <path d="M17 12c2-1 4 0 5 2l3 6c1 2 0 3-1 4l-2 2c1 4 5 8 9 9l2-2c1-1 2-2 4-1l6 3c2 1 3 3 2 5l-2 3c-2 2-5 3-9 1-8-4-15-11-19-19-2-4-1-7 1-9z" fill="var(--paper)"/>
    </svg>
    <span>478-555-0142</span>
  </div>

  <div class="devices" role="img" aria-label="Laptop, tablet and phone showing the online rental website"></div>

  <svg class="location-arrow" width="590" height="130" viewBox="0 0 590 130" aria-hidden="true">
    <polygon points="0,65 60,0 60,20 580,20 580,110 60,110 60,130" fill="var(--navy)"/>
  </svg>
  <div class="address">
    <svg width="24" height="34" viewBox="0 0 26 36" aria-hidden="true">
      <path d="M13 0C6 0 0 6 0 13c0 9 13 23 13 23s13-14 13-23C26 6 20 0 13 0z" fill="var(--paper)"/>
      <circle cx="13" cy="13" r="5" fill="var(--navy)"/>
    </svg>
    <span>210 Maple Ridge Drive</span>
  </div>

  <div class="website">
    <svg width="34" height="34" viewBox="0 0 34 34" aria-hidden="true" fill="none" stroke="var(--navy)" stroke-width="2">
      <circle cx="17" cy="17" r="15"/>
      <ellipse cx="17" cy="17" rx="7" ry="15"/>
      <line x1="2" y1="17" x2="32" y2="17"/>
      <line x1="5" y1="9" x2="29" y2="9"/>
      <line x1="5" y1="25" x2="29" y2="25"/>
    </svg>
    <span>PatGreeneStorage.com</span>
  </div>
</main>
</body>
</html>
```